Brookfen 14 Industrial Park Needs Website

We are looking for a website for a new project we are working on.
Project does not have a logo so just use text. Needs to be responsive and mobile friendly for all browsers and coded for both Android & IOS. SEO is also important. Want something visually grabbing that displays growth, quality and confidence.
WordPress or Joomla – must be desktop and mobile friendly with fast page load speed. Need the ability to edit ourselves.
See attached website brief for further information.
Industry/Entity Type
Land Sale/Lease/Development
Coding
Coded - Design and coding required
Number of Pages Required
4 page
Look and feel
Each slider illustrates characteristics of the customer's brand and the style your logo design should communicate.

```html
<!DOCTYPE html>
<html lang="en">
<head>
<meta charset="utf-8">
<title>Brookfen 14 – Real Estate Development</title>
<link href="https://fonts.googleapis.com/css2?family=Playfair+Display:wght@700&family=Poppins:wght@400;500&display=swap" rel="stylesheet">
<style>
  :root {
    --brand-blue: #0056ad;
    --ink: #1c1c1c;
    --hero-bg: #e8eff8;
    --white: #ffffff;
    --map-tone-a: #ece6dc;
    --map-tone-b: #dbe8f0;
    --divider: rgba(255,255,255,0.35);
  }
  * { box-sizing: border-box; margin: 0; padding: 0; }
  html, body { width: 1200px; height: 950px; overflow: hidden; }
  body { font-family: "Poppins", sans-serif; color: var(--ink); background: var(--white); position: relative; }
  a { color: inherit; text-decoration: none; }

  .top-bar { height: 42px; background: var(--brand-blue); display: flex; align-items: center; justify-content: space-between; padding: 0 141px; color: var(--white); }
  .contact-mail { display: flex; align-items: center; gap: 8px; font-size: 13px; }
  .mail-badge { width: 27px; height: 27px; border-radius: 50%; background: var(--white); display: flex; align-items: center; justify-content: center; }
  .social-list { display: flex; gap: 9px; list-style: none; }
  .social-dot { width: 27px; height: 27px; border-radius: 50%; background: var(--white); display: block; }

  .site-header { height: 80px; display: flex; align-items: center; justify-content: space-between; padding: 0 141px; background: var(--white); }
  .wordmark-name { font-family: "Playfair Display", serif; font-weight: 700; font-size: 37px; line-height: 1; color: var(--brand-blue); }
  .wordmark-tag { font-size: 13.5px; margin-top: 4px; }
  .main-nav { display: flex; align-items: center; gap: 36px; font-size: 13px; }
  .main-nav .is-active { color: var(--brand-blue); font-weight: 500; }
  .btn { display: inline-flex; align-items: center; justify-content: center; background: var(--brand-blue); color: var(--white); border-radius: 21px; font-size: 13px; height: 42px; }
  .btn-contact { width: 95px; }

  .hero { position: absolute; top: 122px; left: 0; width: 1200px; height: 637px; background: var(--hero-bg); }
  .map-frame { position: absolute; left: 134px; top: 86px; width: 424px; height: 466px; border-left: 2px solid var(--brand-blue); border-top: 2px solid var(--brand-blue); border-radius: 12px 12px 0 12px; }
  .map-area { position: absolute; left: 141px; top: 93px; width: 417px; height: 458px; border-radius: 0 12px 12px 0; background: linear-gradient(135deg, var(--map-tone-a), var(--map-tone-b)); }
  .about { position: absolute; left: 642px; top: 176px; width: 420px; }
  .about-title { font-family: "Playfair Display", serif; font-weight: 700; font-size: 34px; line-height: 1.2; color: #2a2a2a; }
  .about-title span { color: var(--brand-blue); }
  .about-text { font-size: 13.3px; line-height: 22.6px; margin-top: 14px; }
  .btn-learn { width: 113px; margin-top: 40px; }

  .site-footer { position: absolute; top: 759px; left: 0; width: 1200px; height: 191px; background: var(--brand-blue); color: var(--white); padding: 0 141px; }
  .footer-main { display: flex; align-items: center; justify-content: space-between; height: 135px; }
  .site-footer .wordmark-name { color: var(--white); }
  .footer-nav { display: flex; gap: 36px; font-size: 13px; margin-left: 60px; }
  .footer-bottom { border-top: 1px solid var(--divider); display: flex; align-items: center; justify-content: space-between; height: 56px; font-size: 13px; }
</style>
</head>
<body>
  <div class="top-bar">
    <a class="contact-mail" href="#">
      <span class="mail-badge">
        <svg width="14" height="11" viewBox="0 0 14 11"><rect x="0.5" y="0.5" width="13" height="10" rx="1.5" fill="#0056ad"/><path d="M1 1.5 L7 6 L13 1.5" stroke="#fff" stroke-width="1.3" fill="none"/></svg>
      </span>
      info@brookfen14.com
    </a>
    <ul class="social-list">
      <li><a class="social-dot" href="#" aria-label="Social profile one"></a></li>
      <li><a class="social-dot" href="#" aria-label="Social profile two"></a></li>
      <li><a class="social-dot" href="#" aria-label="Social profile three"></a></li>
      <li><a class="social-dot" href="#" aria-label="Social profile four"></a></li>
    </ul>
  </div>

  <header class="site-header">
    <div class="wordmark">
      <div class="wordmark-name">Brookfen 14</div>
      <div class="wordmark-tag">Real Estate Development</div>
    </div>
    <nav class="main-nav">
      <a class="is-active" href="#">Home</a>
      <a href="#">Why St. Paul</a>
      <a href="#">Lot Layout</a>
      <a class="btn btn-contact" href="#">Contact</a>
    </nav>
  </header>

  <section class="hero">
    <div class="map-frame"></div>
    <div class="map-area" role="img" aria-label="Regional map showing the Town of St. Paul and surrounding lakes, highways and communities"></div>
    <div class="about">
      <h1 class="about-title">About <span>Brookfen 14</span></h1>
      <p class="about-text">The property is located on the west side of the Town of St. Paul, a growing municipality located northeast of Edmonton, with a regional population of 13,649. The area has a very strong local economy due to its location between Edmonton and Cold Lake, but with a stronger agricultural base. It serves as the focal point for the Smoky Lake area, with an unemployment rate of 5.0% lower than the provincial average of 8.2%.</p>
      <a class="btn btn-learn" href="#">Learn More</a>
    </div>
  </section>

  <footer class="site-footer">
    <div class="footer-main">
      <div class="wordmark">
        <div class="wordmark-name">Brookfen 14</div>
        <div class="wordmark-tag">Real Estate Development</div>
      </div>
      <nav class="footer-nav">
        <a href="#">Home</a>
        <a href="#">Why St. Paul</a>
        <a href="#">Lot Layout</a>
        <a href="#">Contact</a>
      </nav>
      <a class="contact-mail" href="#">
        <span class="mail-badge">
          <svg width="14" height="11" viewBox="0 0 14 11"><rect x="0.5" y="0.5" width="13" height="10" rx="1.5" fill="#0056ad"/><path d="M1 1.5 L7 6 L13 1.5" stroke="#fff" stroke-width="1.3" fill="none"/></svg>
        </span>
        info@brookfen14.com
      </a>
    </div>
    <div class="footer-bottom">
      <span>© 2024 Brookfen14. All Rights Reserved.</span>
      <ul class="social-list">
        <li><a class="social-dot" href="#" aria-label="Social profile one"></a></li>
        <li><a class="social-dot" href="#" aria-label="Social profile two"></a></li>
        <li><a class="social-dot" href="#" aria-label="Social profile three"></a></li>
        <li><a class="social-dot" href="#" aria-label="Social profile four"></a></li>
      </ul>
    </div>
  </footer>
</body>
</html>
```